Company Profile for Consulting Comany

Need Company profile to be designed in a professional way.

for inspiring :-
https://www.folivane.net/gallery/5372904/COMPANY-PROFILE
https://www.folivane.net/gallery/60391742/Biotech-Product-Catalog-No1-(Laminar-Air-Flow)
https://www.folivane.net/gallery/73905218/MPG-Globalpath-Company-Profile-2014-(MPG-Rebrand-part-2)

Target Market(s)

Corporate

Industry/Entity Type

It Company

Font styles to use
Sans Serif

Requirements
Must have
• Landscape A4 size
• Must go with the logo branding
• Must Have Visual Identity is the most important
• Must Have mpty spaces

```html
<!DOCTYPE html>
<html lang="en">
<head>
<meta charset="utf-8">
<title>Pivot Actions – Company Profile Spread</title>
<link href="https://fonts.googleapis.com/css2?family=Raleway:ital,wght@0,300;0,400;0,500;1,300;1,400&display=swap" rel="stylesheet">
<style>
  :root {
    --bg: #e9e9e9;
    --panel: #050505;
    --accent: #2aa6d6;
    --text-light: #e6e6e6;
    --rule: #9a9a9a;
    --photo-light: #f4f4f4;
    --photo-mid: #c9c9c9;
  }
  * { margin: 0; padding: 0; box-sizing: border-box; }
  html, body { width: 1200px; height: 880px; overflow: hidden; background: var(--bg); }
  body { font-family: "Raleway", sans-serif; color: var(--text-light); }

  .spread {
    position: absolute; left: 40px; top: 242px;
    width: 1120px; height: 396px;
    display: flex;
    box-shadow: 0 12px 30px rgba(0,0,0,.18);
  }
  .page { position: relative; width: 560px; height: 100%; display: flex; }
  .page--left { border-right: 1px solid #d4d4d4; }

  .panel { background: var(--panel); width: 300px; height: 100%; }
  .photo {
    flex: 1; height: 100%;
    background: linear-gradient(180deg, var(--photo-light) 0%, #e2e2e2 60%, var(--photo-mid) 100%);
  }
  .page--left .photo { background: linear-gradient(90deg, var(--photo-light) 0%, #d6d6d6 100%); }
  .page--right .photo { background: linear-gradient(90deg, #d6d6d6 0%, var(--photo-light) 100%); }

  /* Why panel */
  .why { padding: 96px 26px 0 40px; }
  .why__title {
    font-weight: 300; font-style: italic; text-transform: uppercase;
    color: var(--accent); font-size: 23px; line-height: 1.15; letter-spacing: .5px;
    margin-bottom: 18px;
  }
  .why__item {
    font-style: italic; text-transform: uppercase; font-size: 6.6px; line-height: 1.3;
    margin-bottom: 8px; letter-spacing: .1px;
  }
  .why__label { color: var(--accent); }

  /* What panel */
  .what { padding: 26px 24px 0 24px; }
  .what__title {
    font-weight: 300; text-transform: uppercase; color: var(--accent);
    font-size: 21px; letter-spacing: .5px; margin-bottom: 12px;
  }
  .what__heading {
    font-weight: 400; text-transform: uppercase; color: var(--accent);
    font-size: 10.5px; padding-bottom: 2px; border-bottom: 1px solid var(--rule);
    margin-bottom: 4px;
  }
  .what__section + .what__section { margin-top: 12px; }
  .what__body { font-size: 6.4px; line-height: 1.3; }
  .what__list { list-style: none; font-size: 6.4px; line-height: 1.3; margin-top: 1px; }
  .what__list li::before { content: "■"; color: var(--accent); font-size: 4px; margin-right: 4px; vertical-align: middle; }
  .what__sub { color: var(--accent); text-transform: uppercase; font-size: 6.2px; margin-top: 8px; }
</style>
</head>
<body>
  <main class="spread">
    <section class="page page--left">
      <div class="panel why">
        <h2 class="why__title">Why<br>Pivot Actions?</h2>
        <p class="why__item"><span class="why__label">Success</span> We will deliver reliable results for you, as our services record shows. In the past few years, we have helped a numbers of organizations with a less than 2% rejection rate.</p>
        <p class="why__item"><span class="why__label">Targeting</span> We understand the importance of targeting the right people and community, the right way. We will work with you to understand the importance of communication and how you can focus the right individual at a good time.</p>
        <p class="why__item"><span class="why__label">Superior workforce</span> Our dedicated training professionals have all been rigorously screened and training to perform at their peak level. They know that they represent our company at all times and understand the importance of enhancing your image.</p>
        <p class="why__item"><span class="why__label">Flexible multichannel abilities</span> Our wide capabilities give an extensive reach and the ability to create exactly the right program and deliver it where it will get the best results.</p>
        <p class="why__item"><span class="why__label">Cost effectiveness</span> Pivot Action will train your staff by offering very affordable value-added projects.</p>
      </div>
      <div class="photo" role="img" aria-label="Soft-focus black and white photo: silhouette of a consultant seated in a chair, gesturing in conversation"></div>
    </section>

    <section class="page page--right">
      <div class="photo" role="img" aria-label="Soft-focus black and white photo: silhouette of a client seated opposite, listening"></div>
      <div class="panel what">
        <h2 class="what__title">What we do?</h2>
        <div class="what__section">
          <h3 class="what__heading">HR &amp; OD Consultation</h3>
          <p class="what__body">Our dedicated team of HR and OD experts is on hand to provide professional support for your HR and OD operations and development. Working closely alongside your organization, we will identify gaps in your current situation, and propose solutions to overcome these issues.</p>
          <ul class="what__list">
            <li>HR Strategy Alignment</li>
            <li>Organizational Design &amp; development</li>
            <li>Talent Assessment &amp; Management</li>
            <li>Learning &amp; Leadership Development</li>
            <li>Communication &amp; Change Management</li>
            <li>Compensation &amp; Benefits</li>
            <li>Work-life initiatives</li>
            <li>Performance &amp; Recognition</li>
            <li>Development &amp; Career Opportunities</li>
            <li>Coaching &amp; Mentoring Program</li>
          </ul>
        </div>
        <div class="what__section">
          <h3 class="what__heading">Professional Training</h3>
          <p class="what__body">Our vocational training services will enable people and organizations to optimize the skills, knowledge, and abilities of its workforce. We deliver a broad range of training courses, including professional qualifications, short courses, and customized training.</p>
          <p class="what__sub">In-house custom training:</p>
          <p class="what__body">We are committed to provide a high-quality training that adds value to our client's employees and their business processes. Too many reasons make our training programs different and deserve the attention given from too many professionals.</p>
          <p class="what__sub">Professional qualifications:</p>
          <p class="what__body">We are proud to introduce a golden portfolio of prestigious vocational qualifications that are globally recognized for its significant benefit to the knowledge, skills, and competencies of certificates holder. The majority of them are introduced in Saudi Market.</p>
        </div>
      </div>
    </section>
  </main>
</body>
</html>
```